Stridewell-Vx Fitness Services Poster

We need a poster to promote our fitness companies' services within one of our off-site facilities. This facility is a student housing complex. The poster will go in the facility gym. We are hosting classes there but would like to advertise the following:
- On-Site Personal Training
- Small Group Training
- Private Yoga Sessions
- Nutrition Coaching

Our website can provide you with the color and themes that we use. However, we would like the poster to be more "KJ Motion" style and less power lifting/crossfit style like our website.

```html
<!DOCTYPE html>
<html lang="en">
<head>
<meta charset="utf-8">
<title>Stridewell-Vx — Home Gym Heroes</title>
<link href="https://fonts.googleapis.com/css2?family=Bebas+Neue&display=swap" rel="stylesheet">
<style>
  :root {
    --ink: #1f1d1e;
    --white: #ffffff;
    --green: #00a651;
    --orange: #f07232;
    --ring: rgba(255, 226, 110, 0.32);
    --gym-dark: #1c2326;
    --gym-mid: #5d6b6e;
  }
  * { margin: 0; padding: 0; box-sizing: border-box; }
  html, body { width: 849px; height: 1200px; overflow: hidden; background: var(--white); }
  .poster {
    position: relative; width: 849px; height: 1200px; overflow: hidden;
    background: var(--white);
    font-family: "Bebas Neue", "Oswald", sans-serif;
  }
  .hero-photo {
    position: absolute; left: 0; top: 0; width: 849px; height: 720px;
    background: linear-gradient(135deg, var(--gym-dark) 0%, #3a4548 40%, var(--gym-mid) 70%, #2b3336 100%);
  }
  .bands { position: absolute; left: 0; top: 0; }
  .brand-box {
    position: absolute; left: 523px; top: 0; width: 297px; height: 285px;
    background: #0d0b0c;
    display: flex; align-items: center; justify-content: center; gap: 10px;
  }
  .brand-box .mark { width: 14px; height: 14px; background: var(--orange); }
  .brand-box .name { color: var(--orange); font-size: 44px; letter-spacing: 1px; }
  .headline {
    position: absolute; left: 0; width: 849px; top: 290px;
    text-align: center; color: var(--white);
    font-size: 142px; line-height: 1; letter-spacing: 1px;
    text-shadow: 4px 6px 8px rgba(0,0,0,0.55);
  }
  .service-photo {
    position: absolute; width: 298px; height: 298px; border-radius: 50%;
  }
  .service-photo.training { left: 68px; top: 486px; background: radial-gradient(circle at 45% 35%, #4a3a33 0%, #1a1515 45%, #0b0a0a 100%); }
  .service-photo.yoga { left: 481px; top: 486px; background: radial-gradient(circle at 50% 30%, #ffe3a3 0%, #f3a24a 40%, #9a5a2a 80%, #3b2416 100%); }
  .subhead {
    position: absolute; left: 0; width: 849px; top: 846px;
    text-align: center; color: var(--ink); font-size: 78px; line-height: 1;
  }
  .services { position: absolute; top: 932px; width: 300px; }
  .services.left { left: 127px; }
  .services.right { left: 447px; }
  .services li {
    list-style: none; height: 39px; display: flex; align-items: center;
    padding-left: 8px; color: var(--white); font-size: 31px; line-height: 1;
  }
  .services li::before {
    content: ""; width: 11px; height: 11px; border-radius: 50%;
    background: var(--white); margin-right: 6px; flex: none;
  }
  .services li.dark { background: var(--ink); }
  .services li.accent { background: var(--orange); }
  .services.right li { padding-left: 30px; }
  .motto {
    position: absolute; left: 0; width: 849px; top: 1040px;
    text-align: center; color: var(--ink); font-size: 66px; line-height: 1;
  }
  .web {
    position: absolute; left: 294px; top: 1106px; width: 266px; height: 40px;
    border-radius: 20px; background: var(--green); color: var(--white);
    display: flex; align-items: center; justify-content: center;
    font-size: 25px; letter-spacing: 3px;
  }
</style>
</head>
<body>
<div class="poster">
  <div class="hero-photo" role="img" aria-label="Athlete crouching at a loaded barbell in a dim gym, chalked hands and wrist wraps"></div>

  <svg class="bands" width="849" height="1200" viewBox="0 0 849 1200" aria-hidden="true">
    <polygon points="0,526 849,395 849,588 0,705" fill="var(--green)"/>
    <polygon points="0,705 849,588 849,735 0,895" fill="var(--orange)"/>
    <circle cx="217" cy="635" r="176" fill="var(--ring)"/>
    <circle cx="630" cy="635" r="176" fill="var(--ring)"/>
  </svg>

  <div class="brand-box">
    <span class="mark"></span>
    <span class="name">Stridewell-Vx</span>
  </div>

  <h1 class="headline">Home Gym Heroes</h1>

  <div class="service-photo training" role="img" aria-label="Muscular man in a push-up position against a dark background"></div>
  <div class="service-photo yoga" role="img" aria-label="Silhouette of a woman meditating cross-legged by a lake at sunset"></div>

  <h2 class="subhead">Build Your Home Gym</h2>

  <ul class="services left">
    <li class="dark">On-Site Personal Training</li>
    <li class="accent">Small Group Training</li>
  </ul>
  <ul class="services right">
    <li class="dark">Private Yoga Sessions</li>
    <li class="accent">Nutrition Coaching</li>
  </ul>

  <p class="motto">Never Give Up</p>
  <p class="web">www.stridewellvx.com</p>
</div>
</body>
</html>
```